Awesome Web Design Project

must have a link to mingleton of the homepage preferably a scrolling view of our mingleton page!

We are an exciting new electrical company with a strong focus on energy efficiency and offering the latest technologies.

The design should allow easy navigation, there shouldn't be too many menus, It should look clean and sleek, Colours to consider could be green, silver/chrome, black,

The site should convey technology, efficiency and simplicity

Must be viewable on all devices, pc's, tablets, phones ie Responsive
Updates

Logo and some pics uploaded!

Industry/Entity Type

Electrical

Requirements
Must have
• must include the following pages,
about us
our services
gallery
contact us
Connect with us
Nice to have
• Would be great if the website design used a user friendly cms,
Should not have
• too many links, menus, clutter it should be clean and easy to navigate

```html
<!DOCTYPE html>
<html lang="en">
<head>
<meta charset="utf-8">
<title>The Electrical Company</title>
<link href="https://fonts.googleapis.com/css2?family=Tinos:ital,wght@0,400;0,700;1,400&display=swap" rel="stylesheet">
<style>
:root{
  --hero-deep:#03324f;
  --hero-mid:#0a6d98;
  --hero-glow:#7fe6f2;
  --nav-bar:#9a9080;
  --nav-text:#ffffff;
  --nav-active:#2ed3f0;
  --headline:#6e6862;
  --welcome-bg:#f8f7f2;
  --welcome-quote:#1c9bc0;
  --muted:#9c9484;
  --content-bg:#e3e0cb;
  --content-line:#d9d5bd;
  --ink:#1e1e1e;
  --thumb-frame:#1479ad;
  --panel:#f2f1ec;
  --field:#e3e0cb;
  --cyan-top:#3fd0ec;
  --cyan-bottom:#0b8fb8;
  --button:#0a7fb0;
  --button-edge:#066690;
  --pill:#a9a07c;
  --footer-bg:#faf9f6;
  --footer-link:#7b7468;
  --icon:#2b2b2b;
  --dot:#a9a07c;
  --dot-active:#0a86c0;
}
*{margin:0;padding:0;box-sizing:border-box}
html,body{width:1194px;height:1200px;overflow:hidden}
body{font-family:"Tinos","Times New Roman",serif;background:var(--footer-bg);position:relative}
.hero{position:absolute;left:0;top:0;width:1194px;height:483px;
  background:radial-gradient(circle at 200px 290px,#ffffff 0,#e9fbff 60px,var(--hero-glow) 110px,rgba(20,150,200,.6) 200px,transparent 320px),
  radial-gradient(ellipse at 900px 260px,#1bb6d6 0,#0b6f9e 250px,transparent 520px),
  linear-gradient(180deg,var(--hero-mid),var(--hero-deep));}
.hero-photo{position:absolute;inset:0}
.nav{position:absolute;left:98px;top:32px;width:1096px;height:66px;background:var(--nav-bar);
  box-shadow:-4px 6px 10px rgba(0,0,0,.35);display:flex;justify-content:flex-end;align-items:center;padding-right:68px;gap:55px}
.nav a{color:var(--nav-text);text-decoration:none;font-size:17px;text-transform:uppercase}
.nav a.active{color:var(--nav-active)}
.headline{position:absolute;left:96px;top:200px;color:var(--headline);font-weight:700;font-size:53px;line-height:64px;letter-spacing:-1.5px}
.headline span{display:block}
.headline .indent{padding-left:54px}
.slider-dots{position:absolute;left:541px;top:457px;width:118px;height:26px;background:#fff;border-radius:8px 8px 0 0;display:flex;justify-content:center;align-items:center;gap:4px}
.slider-dots i{width:24px;height:22px;border-radius:50%;background:var(--dot)}
.slider-dots i.active{background:var(--dot-active)}
.welcome{position:absolute;left:0;top:483px;width:1194px;height:131px;background:var(--welcome-bg);text-align:center}
.welcome-quote{position:absolute;left:170px;top:28px;font-size:28px;color:var(--welcome-quote);white-space:nowrap}
.welcome-sub{position:absolute;left:244px;top:70px;font-size:20px;color:var(--muted);white-space:nowrap}
.content{position:absolute;left:0;top:614px;width:1194px;height:427px;background:var(--content-bg);
  background-image:repeating-linear-gradient(0deg,transparent 0 3px,var(--content-line) 3px 4px),repeating-linear-gradient(90deg,transparent 0 3px,rgba(0,0,0,.025) 3px 4px);
  border-bottom:6px solid #cfcbb4}
.col-title{position:absolute;top:62px;font-size:19px;color:var(--ink);text-transform:uppercase;letter-spacing:-.5px}
.projects{position:absolute;left:94px;top:106px}
.project{display:flex;gap:16px;height:83px}
.project-thumb{width:71px;height:69px;border:6px solid var(--thumb-frame);border-radius:6px;background:linear-gradient(180deg,#9bb4d4,#4a5f86)}
.project-thumb.warm{background:linear-gradient(180deg,#e9c98b,#6c5a45)}
.project h3{font-weight:400;font-size:17px;color:var(--ink);margin-top:0;letter-spacing:-.4px}
.project p{font-style:italic;font-size:14px;line-height:17px;color:var(--muted);width:110px}
.what-text{position:absolute;left:472px;top:103px;width:252px;font-size:11.5px;line-height:15px;color:#7d776c}
.what-photo{position:absolute;left:468px;top:186px;width:247px;height:149px;border:2px solid #f4f3ee;background:linear-gradient(135deg,#3a4d72,#16233d 60%,#5e7ca3)}
.login{position:absolute;left:824px;top:106px;width:274px;height:235px;background:var(--panel);border-radius:0 0 14px 14px;overflow:hidden}
.login-head{height:39px;background:linear-gradient(180deg,#f5fdff 0,var(--cyan-top) 30%,var(--cyan-bottom));padding-left:28px;font-size:30px;font-weight:700;color:var(--ink);line-height:40px}
.field{position:absolute;left:30px;width:233px;height:33px;background:var(--field);color:var(--muted);font-size:15px;line-height:33px;padding-left:6px}
.field.user{top:69px}.field.pass{top:114px}
.login-button{position:absolute;left:25px;top:157px;width:244px;height:40px;border-radius:20px;background:var(--button);border:3px solid var(--button-edge);color:#fff;font-weight:700;font-size:17px;text-align:center;line-height:34px}
.gallery-pill{position:absolute;left:455px;top:1024px;width:277px;height:34px;border-radius:17px;background:var(--pill);color:#fff;font-size:16px;text-align:center;line-height:34px}
.footer-nav{position:absolute;left:254px;top:1076px;display:flex;gap:48px}
.footer-nav a{color:var(--footer-link);text-decoration:none;font-size:15px;text-transform:uppercase}
.social{position:absolute;left:822px;top:1132px;display:flex;gap:10px}
.social span{width:37px;height:37px;border-radius:50%;background:var(--icon);color:#fff;font-size:7.5px;display:flex;align-items:center;justify-content:center}
.social svg{width:37px;height:37px}
</style>
</head>
<body>
<header class="hero">
  <div class="hero-photo" role="img" aria-label="Glowing light bulb among hanging blue bulbs"></div>
  <nav class="nav">
    <a class="active" href="#">Home</a><a href="#">Aboutus</a><a href="#">Services</a><a href="#">Gallery</a><a href="#">Employment</a><a href="#">Contact us</a>
  </nav>
  <h1 class="headline"><span>Lighten Up Your Life!</span><span>The Best Electrical</span><span class="indent">Company</span></h1>
  <div class="slider-dots"><i></i><i class="active"></i><i></i><i></i></div>
</header>

<section class="welcome">
  <p class="welcome-quote">“Welcome to The Electrical Company,here lighten up your life,with the best company”</p>
  <p class="welcome-sub">Loreun lipsum dummy text..Loreun lipsum dummy text..Loreun lipsum dummy text..</p>
</section>

<main class="content">
  <h2 class="col-title" style="left:96px">Latest Projects</h2>
  <div class="projects">
    <div class="project"><div class="project-thumb warm" role="img" aria-label="Power lines at sunset"></div><div><h3>Loreun Lipsum</h3><p>sashajhshas ndbsbd bdfhbb...dbnfbb....tg</p></div></div>
    <div class="project"><div class="project-thumb" role="img" aria-label="Wind turbine"></div><div><h3>Loreun Lipsum</h3><p>sashajhshas ndbsbd bdfhbb...dbnfbb....tg</p></div></div>
    <div class="project"><div class="project-thumb" role="img" aria-label="Electricity pylons"></div><div><h3>Loreun Lipsum</h3><p>sashajhshas ndbsbd bdfhbb...dbnfbb....tg</p></div></div>
  </div>

  <h2 class="col-title" style="left:459px">What we do?</h2>
  <p class="what-text">LLoreun lipsum dummy text..Loreun lipsum dummy text..Loreun lipsum dummy text..Loreun lipsum dummy text..Loreun lipsum dummy text..Loreun lipsum dummy text..Loreun lipsum dummy text..Loreun lipsum dummy text..Loreun lipsum dummy text..Loreun lipsum</p>
  <div class="what-photo" role="img" aria-label="Two engineers working at a digital display"></div>

  <h2 class="col-title" style="left:827px">Connect with us</h2>
  <form class="login">
    <div class="login-head">Login</div>
    <div class="field user">Username</div>
    <div class="field pass">Password</div>
    <div class="login-button">LOGIN</div>
  </form>
</main>

<a class="gallery-pill">Click HereTO Browse The Gallery</a>

<footer>
  <nav class="footer-nav">
    <a href="#">Home</a><a href="#">Aboutus</a><a href="#">Services</a><a href="#">Gallery</a><a href="#">Employment</a><a href="#">Contact us</a>
  </nav>
  <div class="social">
    <span>mingleton</span>
    <span>chirpline</span>
    <span>globeplus</span>
    <span>workweave</span>
    <svg viewBox="0 0 37 37" role="img" aria-label="Inbox"><circle cx="18.5" cy="18.5" r="18.5" fill="#2b2b2b"/><path d="M10 14v10h17V14h-4v6H14v-6z" fill="#fff"/></svg>
    <svg viewBox="0 0 37 37" role="img" aria-label="Feed"><circle cx="18.5" cy="18.5" r="18.5" fill="#2b2b2b"/><circle cx="12.5" cy="24.5" r="2.6" fill="#fff"/><path d="M10 17a10 10 0 0 1 10 10" stroke="#fff" stroke-width="3" fill="none"/><path d="M10 11a16 16 0 0 1 16 16" stroke="#fff" stroke-width="3" fill="none"/></svg>
  </div>
</footer>
</body>
</html>
```